Education Foundation Needs a Flyer for an Awareness/Fundraising Event

We need a flyer design for our Education Celebration that is held each year to commemorate Lone Star Learning Days.

This event provides an excellent opportunity for the community to come together to celebrate the education of our children and support the Brookmere Unified Learning District. All twelve schools in the district will have tabletop displays highlighting some of their activities during the year. Teachers will also have grant displays to spotlight the innovative classroom projects they implemented due to funding provided by the Brookmere Learning Trust.

The evening will also include entertainment provided by BULD school choirs. The event concludes with drawing for prices, and a raffle drawing.

Listed below are the details that need to be included in the flyer. I have also included our logo that must be used. I also included some photos from past celebrations that may or may not be helpful.

Please join the Brookmere Learning Trust as we celebrate BULD and its students, educational programs, and schools.

Thursday, March 26, 2015
5:00 p.m. – 8:00 p.m.
Brookmere Senior Academy

Students: Please sign up to be entered in a drawing for Pixora Mini.
Adults: Please sign up to be entered in a drawing for a $50 Shopwell Gift Card.

Raffle Prizes
KORVAN 50" Class 1080p LED Smart HDTV
Zentra Prime Console w/ Motionbar
Donations of $2 each or 3 for $5, or 7 for $10
*Tickets are available at the BULD Administration Building/ Communications and at the schools. (You must be present to win.)

Prizes Galore!
• Campus with the highest percentage of adult attendance will win $300 + the Traveling
Trophy for one year.
• Campus with the 2nd highest percentage of adult attendance will win $150.
• Additional drawings for Teacher, Principal/ Asst. Principal, and District Personnel will be held.

Your Choice – Your Prize
Drawings

7" Dravik NEBULA Pad 4
Fennix Streamlet
Brewlo Classic B20 Single Serve
External Hard Drive
Brewlo 3.0 B700 Coffee Brewing System w/ Carafe
Fennix Streamlet
Cotton Candy Maker
*For your donation of $1.00 per ticket, you may place your ticket(s) in one or all of the baskets. It’s your choice. (You must be present to win.)

Food!
Hot Dogs $1.00
Corn Dogs $0.75
Chips $0.50
Drinks $0.75
Cookies $0.75
Baskets - $2.50 (Hot Dog or Corn Dog, Chips, Drink, Cookie)

For more information, please call 555-318-2946.

```html
<!DOCTYPE html>
<html lang="en">
<head>
<meta charset="utf-8">
<title>Brookmere Learning Trust – Education Celebration</title>
<link href="https://fonts.googleapis.com/css2?family=Arimo:wght@400;700&display=swap" rel="stylesheet">
<style>
  :root{
    --navy:#1c3a8e;
    --navy-dark:#142b6e;
    --orange-1:#f39019;
    --orange-2:#fbb534;
    --purple-1:#a93db6;
    --purple-2:#6c1c7d;
    --green-1:#46c52c;
    --green-2:#17921a;
    --red-1:#f46a1a;
    --red-2:#bf300d;
    --ink:#1b1b1b;
    --white:#ffffff;
    --gold:#ffc21a;
  }
  *{margin:0;padding:0;box-sizing:border-box}
  html,body{width:907px;height:1200px;overflow:hidden;background:#ffffff}
  body{font-family:"Arimo",Arial,sans-serif;color:var(--ink)}
  .flyer{position:relative;width:907px;height:1200px;overflow:hidden;background:var(--white)}
  .hero-photo{position:absolute;left:0;top:0;width:907px;height:480px;
    background:linear-gradient(120deg,#c98a5f 0%,#e8c6a4 35%,#7a5b7e 60%,#d9cbb8 80%,#9aa6b8 100%)}
  .backdrop{position:absolute;left:0;top:0}
  .brand-tab{position:absolute;left:48px;top:20px;width:210px;height:175px;background:var(--white);
    border-radius:22px 22px 22px 48px;display:flex;flex-direction:column;align-items:center;justify-content:center;gap:12px;
    box-shadow:0 2px 6px rgba(0,0,0,.25)}
  .brand-tab .mark{width:58px;height:58px;border-radius:50%;background:var(--navy)}
  .brand-tab .name{font-weight:700;font-size:21px;line-height:1.15;color:var(--navy);text-align:center}
  .hex{position:absolute;display:flex;align-items:center;justify-content:center;text-align:center;color:var(--white);
    font-size:18.5px;line-height:1.28;font-weight:400}
  .hex svg{position:absolute;left:0;top:0;width:100%;height:100%;filter:drop-shadow(0 2px 4px rgba(0,0,0,.35))}
  .hex .hex-text{position:relative;padding:0 52px}
  .hex-invite{left:30px;top:288px;width:282px;height:246px}
  .hex-date{left:306px;top:344px;width:288px;height:246px}
  .hex-date .hex-text{font-size:19px}
  .hex-signup{left:592px;top:300px;width:280px;height:240px}
  .hex-signup .hex-text{padding:0 40px;font-size:18px;line-height:1.22}
  .hex-signup h3{font-size:19.5px;font-weight:700;margin-top:4px}
  .pill{position:absolute;background:var(--navy);color:var(--white);font-weight:700;font-size:17px;letter-spacing:.3px;
    padding:4px 13px;border-radius:14px;box-shadow:0 1px 3px rgba(0,0,0,.3);white-space:nowrap}
  .pill.large{font-size:19px;padding:6px 14px;border-radius:16px}
  .block{position:absolute;font-size:14.2px;line-height:1.3;color:var(--ink)}
  .block ul{list-style:none}
  .left-col li{position:relative;padding-left:14px}
  .left-col li::before{content:"";position:absolute;left:2px;top:6px;width:6px;height:6px;border-radius:50%;background:var(--white)}
  .right-col{text-align:right}
  .right-col li{position:relative;padding-right:14px}
  .right-col li::after{content:"";position:absolute;right:2px;top:6px;width:6px;height:6px;border-radius:50%;background:var(--white)}
  .note{margin-top:6px}
  .raffle-list{left:26px;top:586px;width:440px}
  .galore-list{left:26px;top:764px;width:440px}
  .drawings-list{right:40px;top:600px;width:480px}
  .food-list{right:40px;top:834px;width:300px}
  .photo-hex{position:absolute;width:178px;height:166px}
  .photo-hex svg{width:100%;height:100%;filter:drop-shadow(0 2px 4px rgba(0,0,0,.35))}
  .contact{position:absolute;left:0;width:907px;top:1136px;text-align:center;color:var(--white);font-size:23px;font-weight:700}
  .contact .phone{color:var(--gold);font-size:32px;margin-left:4px}
</style>
</head>
<body>
<div class="flyer">
  <div class="hero-photo" role="img" aria-label="Photo of smiling students and parents at a past celebration"></div>

  <svg class="backdrop" width="907" height="1200" viewBox="0 0 907 1200" aria-hidden="true">
    <defs>
      <linearGradient id="orangeFill" x1="0" y1="0" x2="1" y2="1">
        <stop offset="0" stop-color="var(--orange-1)"/>
        <stop offset="1" stop-color="var(--orange-2)"/>
      </linearGradient>
      <linearGradient id="navyFill" x1="0" y1="0" x2="0" y2="1">
        <stop offset="0" stop-color="#2448a6"/>
        <stop offset="1" stop-color="var(--navy-dark)"/>
      </linearGradient>
    </defs>
    <path d="M0,380 C300,392 620,425 907,448 L907,1200 L0,1200 Z" fill="#ffffff"/>
    <path d="M0,390 C300,402 620,435 907,458 L907,1200 L0,1200 Z" fill="url(#navyFill)"/>
    <path d="M0,402 C300,414 620,447 907,470 L907,1200 L0,1200 Z" fill="#ffffff"/>
    <path d="M0,410 C300,422 620,455 907,478 L907,1200 L0,1200 Z" fill="url(#orangeFill)"/>
    <path d="M0,968 Q453,1082 907,968 L907,1200 L0,1200 Z" fill="#ffffff"/>
    <path d="M0,980 Q453,1094 907,980 L907,1200 L0,1200 Z" fill="url(#navyFill)"/>
  </svg>

  <div class="brand-tab">
    <div class="mark"></div>
    <div class="name">Brookmere<br>Learning Trust</div>
  </div>

  <div class="hex hex-invite">
    <svg viewBox="0 0 282 246" preserveAspectRatio="none" aria-hidden="true">
      <defs><linearGradient id="gPurple" x1="0" y1="0" x2="0" y2="1"><stop offset="0" stop-color="var(--purple-1)"/><stop offset="1" stop-color="var(--purple-2)"/></linearGradient></defs>
      <polygon points="72,6 210,6 276,123 210,240 72,240 6,123" fill="url(#gPurple)" stroke="#fff" stroke-width="6" stroke-linejoin="round"/>
    </svg>
    <p class="hex-text">Please join the Brookmere Learning Trust as we celebrate BULD and its students, educational programs and schools</p>
  </div>

  <div class="hex hex-date">
    <svg viewBox="0 0 288 246" preserveAspectRatio="none" aria-hidden="true">
      <defs><linearGradient id="gGreen" x1="0" y1="0" x2="0" y2="1"><stop offset="0" stop-color="var(--green-1)"/><stop offset="1" stop-color="var(--green-2)"/></linearGradient></defs>
      <polygon points="74,6 214,6 282,123 214,240 74,240 6,123" fill="url(#gGreen)" stroke="#fff" stroke-width="6" stroke-linejoin="round"/>
    </svg>
    <p class="hex-text">Thursday,<br>March 26, 2015<br>5:00 p.m. – 8:00 p.m.<br>Brookmere Senior Academy</p>
  </div>

  <div class="hex hex-signup">
    <svg viewBox="0 0 280 240" preserveAspectRatio="none" aria-hidden="true">
      <defs><linearGradient id="gRed" x1="0" y1="0" x2="0" y2="1"><stop offset="0" stop-color="var(--red-1)"/><stop offset="1" stop-color="var(--red-2)"/></linearGradient></defs>
      <polygon points="70,6 210,6 274,120 210,234 70,234 6,120" fill="url(#gRed)" stroke="#fff" stroke-width="6" stroke-linejoin="round"/>
    </svg>
    <div class="hex-text">
      <h3>Students:</h3>
      <p>Please sign up to be entered in a drawing for Pixora Mini.</p>
      <h3>Adults:</h3>
      <p>Please sign up to be entered in a drawing for a $50 Shopwell Gift Card</p>
    </div>
  </div>

  <div class="pill" style="left:26px;top:552px">RAFFLE PRIZES</div>
  <div class="block left-col raffle-list">
    <ul>
      <li>KORVAN 50" Class 1080p LED Smart HDTV</li>
      <li>Zentra Prime Console w/ Motionbar</li>
      <li>Donations of $2 each or 3 for $5, or 7 for $10</li>
    </ul>
    <p class="note">*Tickets are available at the BULD Administration<br>Building/ Communications and at the schools.<br>(You must be present to win.)</p>
  </div>

  <div class="pill" style="left:26px;top:728px">PRIZES GALORE!</div>
  <div class="block left-col galore-list">
    <ul>
      <li>Campus with the highest percentage of adult attendance will win $300 + the Traveling Trophy for one year.</li>
      <li>Campus with the 2nd highest percentage of adult attendance will win $150.</li>
      <li>Additional drawings for Teacher, Principal/ Asst. Principal, and District Personnel will be held.</li>
    </ul>
  </div>

  <div class="pill large" style="left:26px;top:906px">YOUR CHOICE – YOUR PRIZE</div>

  <div class="pill" style="right:30px;top:557px">DRAWINGS</div>
  <div class="block right-col drawings-list">
    <ul>
      <li>7" Dravik NEBULA Pad 4</li>
      <li>Fennix Streamlet</li>
      <li>Brewlo Classic B20 Single Serve</li>
      <li>External Hard Drive</li>
      <li>Brewlo 3.0 B700 Coffee Brewing System w/ Carafe</li>
      <li>Fennix Streamlet</li>
      <li>Cotton Candy Maker</li>
    </ul>
    <p class="note" style="padding-right:14px">*For your donation of $1.00 per ticket, you may place your ticket(s) in one or all of the baskets. It's your choice. (You must be present to win.)</p>
  </div>

  <div class="pill" style="right:30px;top:798px">FOOD!</div>
  <div class="block right-col food-list">
    <ul>
      <li>Hot Dogs $1.00</li>
      <li>Corn Dogs $0.75</li>
      <li>Chips $0.50</li>
      <li>Drinks $0.75</li>
      <li>Cookies $0.75</li>
      <li>Baskets - $2.50 (Hot Dog or Corn Dog,<br>Chips, Drink, Cookie)</li>
    </ul>
  </div>

  <div class="photo-hex" style="left:126px;top:958px" role="img" aria-label="Photo of a student using a microscope with a teacher">
    <svg viewBox="0 0 178 166" aria-hidden="true">
      <defs><linearGradient id="p1" x1="0" y1="0" x2="1" y2="1"><stop offset="0" stop-color="#d8d3cc"/><stop offset="1" stop-color="#7d6d66"/></linearGradient></defs>
      <polygon points="46,5 132,5 173,83 132,161 46,161 5,83" fill="url(#p1)" stroke="#fff" stroke-width="6" stroke-linejoin="round"/>
    </svg>
  </div>
  <div class="photo-hex" style="left:350px;top:972px" role="img" aria-label="Photo of children and volunteers at a school display table">
    <svg viewBox="0 0 178 166" aria-hidden="true">
      <defs><linearGradient id="p2" x1="0" y1="0" x2="1" y2="1"><stop offset="0" stop-color="#e06a4a"/><stop offset="1" stop-color="#5a78b0"/></linearGradient></defs>
      <polygon points="46,5 132,5 173,83 132,161 46,161 5,83" fill="url(#p2)" stroke="#fff" stroke-width="6" stroke-linejoin="round"/>
    </svg>
  </div>
  <div class="photo-hex" style="left:586px;top:958px" role="img" aria-label="Photo of a presenter with students in a busy cafeteria">
    <svg viewBox="0 0 178 166" aria-hidden="true">
      <defs><linearGradient id="p3" x1="0" y1="0" x2="1" y2="1"><stop offset="0" stop-color="#c9c2b5"/><stop offset="1" stop-color="#3c5ea8"/></linearGradient></defs>
      <polygon points="46,5 132,5 173,83 132,161 46,161 5,83" fill="url(#p3)" stroke="#fff" stroke-width="6" stroke-linejoin="round"/>
    </svg>
  </div>

  <p class="contact">For more information, please call <span class="phone">555-318-2946</span></p>
</div>
</body>
</html>
```